Create a Graphic About YOURSELF and PixelHarbor

PixelHarbor would like you (designers) to create an awesome graphic to promote YOURSELF and your profile on PixelHarbor!

Your graphic should communicate your name, your services and should mention PixelHarbor.

The design should be perfect for sharing on Chatterly. Here's an example of what we'd like http://blog.pixelharbor-example.ca/article/333/pixelharbor-launches-3000-hire-me-social-design-contest

Once you submitted your design, we'd love you to share the design ('advertisement') and promote yourself and PixelHarbor to your friends and potential customers. So make your submissions great and get your friends to vote for your design by 'Liking' it on Chatterly!

Prizes:
$1500 - "PixelHarbor Community" prize awarded to the designer with the most Chatterly 'Likes'
5 x $50 for the next 5 'most liked' designs on Chatterly

$1000 - "Hire Me" prize awarded to the designer who receives the most client invites
5 x $50 for the next 5 'most invited' designers

In summary, this is a great opportunity for you to increase your exposure to PixelHarbor customers and win cash prizes. Show off your design skills and get hired by PixelHarbor customers from around the world!

Target Market(s)

Fans, friends and customers of YOU

Industry/Entity Type

Cash

Requirements
Must have
• 1) Include your PixelHarbor user name on the graphic so customers can find you in the PixelHarbor Designer Directory
2) Include the tagline "Hire Me on PixelHarbor.com!" in your graphic design.
3) Share your design's URL on our Chatterly wall at http://chatterly-example.com/pixelharbor and get your friends to 'like' your design.
Nice to have
• 1) Include a tagline that expresses your design approach/philosophy
2) Artwork dimensions: 403 x 403 px
3) You can submit more than 1 design!
Should not have
• You must own the copyright of any images you use including stock imagery.

```html
<!DOCTYPE html>
<html lang="en">
<head>
<meta charset="utf-8">
<title>Create. Design. Inspire. — Maren Solvik on PixelHarbor</title>
<link rel="stylesheet" href="https://fonts.googleapis.com/css2?family=Exo+2:wght@400;600;700&display=swap">
<style>
  :root {
    --brand-pink: #ff0f6e;
    --ink-white: #ffffff;
  }
  html, body {
    margin: 0;
    padding: 0;
    width: 1200px;
    height: 1200px;
    overflow: hidden;
    background: var(--brand-pink);
  }
  .promo-card {
    position: relative;
    width: 1200px;
    height: 1200px;
    background: var(--brand-pink);
  }
  .promo-art {
    position: absolute;
    inset: 0;
    width: 1200px;
    height: 1200px;
    display: block;
  }
  .motto-line {
    font-family: "Exo 2", sans-serif;
    font-weight: 600;
    font-size: 232px;
    fill: var(--ink-white);
    letter-spacing: 2px;
  }
  .profile-line {
    font-family: "Exo 2", sans-serif;
    font-size: 46px;
    fill: var(--ink-white);
  }
  .profile-site { font-weight: 400; }
  .profile-name { font-weight: 700; }
</style>
</head>
<body>
  <main class="promo-card">
    <svg class="promo-art" viewBox="0 0 1200 1200" xmlns="http://www.w3.org/2000/svg">
      <g class="motto">
        <text class="motto-line" x="54" y="721" textLength="893" lengthAdjust="spacingAndGlyphs">CREATE.</text>
        <text class="motto-line" x="54" y="908" textLength="875" lengthAdjust="spacingAndGlyphs">DESIGN.</text>
        <text class="motto-line" x="54" y="1087" textLength="944" lengthAdjust="spacingAndGlyphs">INSPIRE.</text>
      </g>
      <text class="profile-line" x="54" y="1164" textLength="905" lengthAdjust="spacingAndGlyphs"><tspan class="profile-site">pixelharbor.com // </tspan><tspan class="profile-name">maren solvik</tspan></text>
    </svg>
  </main>
</body>
</html>
```